Women's Online Clothing Boutique Needs Business Cards

I already have a logo that I would like to use. Some of the things that interest me is black business cards, foil embossed logo, glossy embossed logo, leopard print, no yellow font, rounded edges. I even like just a large logo on the front side with all of my information on the back side.

Contact Information for Business Card

https://silverheron.shopvenlo.com/
https://www.pagelink.net/thesilverheronboutique/
https://www.picfeed.net/thesilverheronboutique/
silverheronboutique@mailora.net

Requirements
Must have
• My Logo
Nice to have
• Leopard Print
Should not have
• No Yellow Font

```html
<!DOCTYPE html>
<html lang="en">
<head>
<meta charset="UTF-8">
<title>The Silver Heron Boutique – Business Card</title>
<link href="https://fonts.googleapis.com/css2?family=Poppins:wght@400;500&display=swap" rel="stylesheet">
<style>
  :root {
    --backdrop: #141416;
    --card: #222527;
    --gold: #d3992b;
    --gold-line: #b8892f;
    --white: #f2f2f2;
  }
  * { margin: 0; padding: 0; box-sizing: border-box; }
  html, body { width: 1200px; height: 800px; overflow: hidden; }
  body {
    background: var(--backdrop);
    font-family: "Poppins", sans-serif;
    display: flex;
    align-items: center;
    justify-content: center;
    gap: 60px;
  }
  .card {
    position: relative;
    width: 520px;
    height: 298px;
    background: var(--card);
    border-radius: 18px;
    box-shadow: 0 18px 40px rgba(0,0,0,.55);
    overflow: hidden;
  }
  .brand {
    position: absolute;
    display: flex;
    flex-direction: column;
    align-items: center;
    color: var(--gold);
    font-weight: 500;
    text-align: center;
  }
  .brand-mark {
    width: 34px; height: 34px;
    border-radius: 50%;
    background: var(--gold);
    margin-bottom: 14px;
  }
  .brand-name { letter-spacing: .04em; line-height: 1.15; }
  .brand-rule { height: 1px; background: var(--gold-line); }

  /* Front */
  .card--front .brand { inset: 0; justify-content: center; }
  .card--front .brand-rule { width: 300px; margin: 14px 0; }
  .card--front .brand-name { font-size: 34px; }
  .card--front .brand-sub { font-size: 16px; letter-spacing: .5em; }

  /* Back */
  .card--back .brand { left: 28px; top: 0; bottom: 0; width: 200px; justify-content: center; }
  .card--back .brand-mark { width: 26px; height: 26px; margin-bottom: 10px; }
  .card--back .brand-name { font-size: 22px; }
  .card--back .brand-rule { width: 170px; margin: 10px 0; }
  .card--back .brand-sub { font-size: 11px; letter-spacing: .45em; }
  .divider {
    position: absolute; left: 246px; top: 50px; bottom: 50px;
    width: 1px; background: var(--gold-line);
  }
  .details { position: absolute; left: 268px; top: 70px; right: 18px; }
  .person-name {
    color: var(--white); font-size: 17px; font-weight: 500;
    letter-spacing: .22em;
  }
  .person-role {
    color: var(--gold); font-size: 10px; letter-spacing: .3em;
    margin-top: 2px;
  }
  .contacts { list-style: none; margin-top: 24px; }
  .contact {
    display: flex; align-items: center; gap: 8px;
    color: var(--white); font-size: 9.5px; line-height: 1;
    margin-bottom: 9px; white-space: nowrap;
  }
  .contact-icon {
    flex: none; width: 15px; height: 15px; border-radius: 2px;
    background: var(--gold);
    display: flex; align-items: center; justify-content: center;
  }
</style>
</head>
<body>
  <section class="card card--front" aria-label="Card front">
    <div class="brand">
      <span class="brand-mark"></span>
      <span class="brand-name">THE SILVER HERON</span>
      <span class="brand-rule"></span>
      <span class="brand-sub">BOUTIQUE</span>
    </div>
  </section>

  <section class="card card--back" aria-label="Card back">
    <div class="brand">
      <span class="brand-mark"></span>
      <span class="brand-name">THE SILVER HERON</span>
      <span class="brand-rule"></span>
      <span class="brand-sub">BOUTIQUE</span>
    </div>
    <div class="divider"></div>
    <div class="details">
      <p class="person-name">CLARA HENSLEY</p>
      <p class="person-role">DIRECTOR</p>
      <ul class="contacts">
        <li class="contact">
          <span class="contact-icon">
            <svg width="10" height="8" viewBox="0 0 10 8"><rect x=".5" y=".5" width="9" height="7" fill="none" stroke="#222527"/><path d="M.5 .5 5 4.5 9.5 .5" fill="none" stroke="#222527"/></svg>
          </span>
          silverheronboutique@mailora.net
        </li>
        <li class="contact">
          <span class="contact-icon"></span>
          pagelink.net/thesilverheronboutique/
        </li>
        <li class="contact">
          <span class="contact-icon"></span>
          picfeed.net/thesilverheronboutique/
        </li>
        <li class="contact">
          <span class="contact-icon">
            <svg width="10" height="10" viewBox="0 0 10 10"><circle cx="5" cy="5" r="4.3" fill="none" stroke="#222527"/><ellipse cx="5" cy="5" rx="1.8" ry="4.3" fill="none" stroke="#222527"/><path d="M.7 5h8.6" stroke="#222527"/></svg>
          </span>
          silverheron.shopvenlo.com
        </li>
      </ul>
    </div>
  </section>
</body>
</html>
```